Bramblewick Keystone

Looking for modern business cards.
Clean contemporary design.
Similar to this.
https://www.snapvorlo.net/imgview?src=https%3A%2F%2Fcdn.printquell.net%2Fprofessional_elegant_modern_black_plain_metal_business_card-a1b2c3d4e5f60718293a4b5c6d7e8f90_qwxyz_4tmpl_540.jpg&ref=https%3A%2F%2Fwww.printquell.net%2Fprofessional_elegant_modern_black_plain_metal_business_card-100200300400500600&id=7aB9cD3e-QR5TU&tid=Xyz_abc123defGH%3A&v=10abcDEFghiJKLmnoPQRstUVwxYZ0123456789abcd..x&w=540&h=540&bih=1360&biw=1061&q=modern%20business%20cards&ref2=0abcDEFghiJKLmnoPQRstUVwxYZ0123456789abcd&ia=mrc&ua=8

But I'd like the blue to look metallic.

```html
<!DOCTYPE html>
<html lang="en">
<head>
<meta charset="utf-8">
<title>Bramblewick Keystone – Business Card</title>
<link href="https://fonts.googleapis.com/css2?family=Lato:wght@400;700&display=swap" rel="stylesheet">
<style>
  :root {
    --backdrop: #3b3532;
    --card: #0e0e10;
    --card-edge: #1a1a1d;
    --blue: #2aa6d6;
    --blue-metal-light: #c4eefc;
    --blue-metal-mid: #2aa6d6;
    --blue-metal-dark: #0f4f69;
    --blue-deep-light: #7fc3de;
    --blue-deep-mid: #1b6e8f;
    --blue-deep-dark: #0b3446;
    --silver: #c9c9cc;
    --text: #e9e9ea;
    --rule: #4a4a4e;
  }
  * { box-sizing: border-box; margin: 0; padding: 0; }
  html, body {
    width: 1200px; height: 900px; overflow: hidden;
    background: var(--backdrop);
    font-family: "Lato", Arial, sans-serif;
  }
  .gradient-defs { position: absolute; width: 0; height: 0; }
  .stage {
    width: 1200px; height: 900px;
    display: flex; align-items: center; justify-content: center; gap: 40px;
  }
  .card {
    position: relative;
    width: 540px; height: 309px;
    background: var(--card);
    border: 1px solid var(--card-edge);
    box-shadow: 0 14px 30px rgba(0,0,0,0.45);
  }
  .metal-blue {
    background: linear-gradient(180deg, var(--blue-metal-light) 0%, var(--blue-metal-mid) 42%, var(--blue-metal-dark) 62%, var(--blue-metal-mid) 82%, var(--blue-metal-light) 100%);
    -webkit-background-clip: text; background-clip: text;
    color: transparent;
  }
  .metal-blue-deep {
    background: linear-gradient(180deg, var(--blue-deep-light) 0%, var(--blue-deep-mid) 42%, var(--blue-deep-dark) 62%, var(--blue-deep-mid) 82%, var(--blue-deep-light) 100%);
    -webkit-background-clip: text; background-clip: text;
    color: transparent;
  }

  /* Front: contact side */
  .brand-front {
    position: absolute; top: 78px; right: 36px;
    display: flex; align-items: center; gap: 10px;
  }
  .brand-dot {
    width: 12px; height: 12px; border-radius: 50%;
    background: var(--blue);
  }
  .brand-name {
    font-weight: 700; font-size: 28px; letter-spacing: 0.2px;
    color: var(--blue);
  }
  .rule {
    position: absolute; height: 1px;
    background: linear-gradient(90deg, rgba(74,74,78,0), var(--rule) 25%, var(--rule));
  }
  .rule-brand { top: 146px; left: 250px; right: 30px; }
  .rule-name { top: 180px; left: 250px; right: 30px; }
  .address {
    position: absolute; top: 192px; right: 40px;
    color: var(--text); font-size: 15px; line-height: 1.4;
    font-style: normal; text-align: left;
  }
  .person {
    position: absolute; left: 40px; bottom: 22px;
  }
  .person-name {
    font-weight: 700; font-size: 21px; letter-spacing: 0.5px;
    text-transform: uppercase; line-height: 26px;
  }
  .person-role { color: var(--text); font-size: 16px; margin-bottom: 6px; }
  .contact-list { list-style: none; }
  .contact-list li {
    display: flex; align-items: center; gap: 9px;
    color: var(--text); font-size: 15px; line-height: 21px;
    padding-left: 20px;
  }
  .contact-list svg { width: 12px; height: 12px; fill: url(#metal-blue-fill); flex: none; }

  /* Back: brand side */
  .brand-back {
    position: absolute; inset: 0;
    display: flex; align-items: center; justify-content: center; gap: 12px;
  }
  .brand-back .brand-dot { background: var(--silver); }
  .brand-back .brand-name { color: var(--silver); font-size: 32px; }
</style>
</head>
<body>
<svg class="gradient-defs" aria-hidden="true">
  <defs>
    <linearGradient id="metal-blue-fill" x1="0" y1="0" x2="0" y2="1">
      <stop offset="0" stop-color="#c4eefc"/>
      <stop offset="0.45" stop-color="#2aa6d6"/>
      <stop offset="0.7" stop-color="#0f4f69"/>
      <stop offset="1" stop-color="#2aa6d6"/>
    </linearGradient>
  </defs>
</svg>
<main class="stage">
  <section class="card card-front">
    <div class="brand-front">
      <span class="brand-dot"></span>
      <span class="brand-name">Bramblewick Keystone</span>
    </div>
    <div class="rule rule-brand"></div>
    <div class="rule rule-name"></div>
    <address class="address">
      17 Larkspur Row<br>Eastmere, 40718
    </address>
    <div class="person">
      <div class="person-name"><span class="metal-blue-deep">Corwin</span> <span class="metal-blue">Ashdale</span></div>
      <div class="person-role">Managing Director</div>
      <ul class="contact-list">
        <li><svg viewBox="0 0 24 24" aria-hidden="true"><path d="M6.6 10.8a15.1 15.1 0 0 0 6.6 6.6l2.2-2.2a1 1 0 0 1 1-.25 11.4 11.4 0 0 0 3.6.57 1 1 0 0 1 1 1V20a1 1 0 0 1-1 1A17 17 0 0 1 3 4a1 1 0 0 1 1-1h3.5a1 1 0 0 1 1 1c0 1.250.2 2.46.57 3.58a1 1 0 0 1-.25 1z"/></svg>444 555 0193</li>
        <li><svg viewBox="0 0 24 24" aria-hidden="true"><path d="M2 5h20v14H2zm2 2v.5l8 5 8-5V7l-8 5z"/></svg>hello@bramblewick.example</li>
        <li><svg viewBox="0 0 24 24" aria-hidden="true"><circle cx="12" cy="12" r="10"/></svg>www.bramblewick.example</li>
      </ul>
    </div>
  </section>

  <section class="card card-back">
    <div class="brand-back">
      <span class="brand-dot"></span>
      <span class="brand-name">Bramblewick Keystone</span>
    </div>
  </section>
</main>
</body>
</html>
```